Online Trading Web-Design

Web design is required for a new startup that specialises in online trading between buyers and sellers of fashion apparel. The company is called: Blue Harbor Commons (bhc)

Website needs to be clean and css friendly. we like the idea of having a largish "banner" on the homepage which we can rotate using HTML5. examples of the banners are: http://au.vextrano.com/ ; http://www.plorvak.com.au/

the logo has been established already, please limit designs around the colors already established (see uploaded logo).
Updates

Hi, a few clarifications:

1. although the website deals in online trading for clothes etc. the main focus of the website needs to be about highlighting trading between buyers (clothing stores) and sellers (clothing brands). so the website wont be directly selling items of clothes etc.

Industry/Entity Type

Fashion

```html
<!DOCTYPE html>
<html lang="en">
<head>
<meta charset="utf-8">
<title>Blue Harbor Commons</title>
<link rel="stylesheet" href="https://fonts.googleapis.com/css2?family=Open+Sans:wdth,wght@75..100,300..700&display=swap">
<style>
:root{
  --ink:#2d2d2d;
  --bar:#111111;
  --header:#2b2b2b;
  --teal:#2e5566;
  --teal-dark:#23434f;
  --page:#f4f4f4;
  --band:#ebebeb;
  --line:#d8d8d8;
  --tab:#d9d9d9;
  --muted:#8a8a8a;
  --text:#555555;
  --white:#ffffff;
  --hot:#d9232a;
}
*{box-sizing:border-box;margin:0;padding:0}
html,body{width:714px;height:1200px;overflow:hidden}
body{position:relative;background:var(--page);font-family:Arial,Helvetica,sans-serif;color:var(--text);font-size:8px;line-height:1.5}
.cond{font-family:"Open Sans",sans-serif;font-stretch:75%;font-weight:300}
.abs{position:absolute}

.topbar{left:0;top:0;width:714px;height:20px;background:var(--bar);display:flex;justify-content:flex-end;align-items:center;gap:9px;padding-right:20px;font-size:7px;color:#bbb}
.topbar .sep{width:1px;height:10px;background:#444}
.topbar .social{width:9px;height:9px;background:#777;border-radius:2px}
.header{left:0;top:20px;width:714px;height:59px;background:var(--header)}
.nav{right:20px;top:30px;font-size:16px;color:var(--white);letter-spacing:.2px}
.nav .active{color:#7fa3b6}
.nav .slash{margin:0 5px}

.slider-area{left:0;top:79px;width:714px;height:244px;background:#f7f7f7;border-bottom:5px solid var(--band)}
.slide-photo{left:22px;top:106px;width:480px;height:133px;background:linear-gradient(90deg,#7a2a6a 0%,#c24e95 30%,#e6d5c8 45%,#1b1b1b 65%,#f0f0f0 82%,#c22a3a 100%)}
.caption{left:22px;top:239px;width:480px;height:63px;background:#333;color:var(--white)}
.caption h2{font-size:14px;text-align:center;margin-top:7px;font-weight:300}
.caption p{font-size:9px;margin:2px 0 0 7px}
.caption .more{position:absolute;right:8px;bottom:7px;font-size:10px;display:flex;align-items:center;gap:4px}
.arrow-box{display:inline-block;width:12px;height:10px;background:var(--teal)}
.tab{left:502px;width:191px;height:48px;background:var(--tab);display:flex;align-items:center;gap:8px;padding-left:7px;font-size:10px;color:#444}
.tab.active{background:var(--teal);color:var(--white)}
.thumb{width:56px;height:36px;border:2px solid var(--white)}

.quote{left:22px;top:350px;width:671px;height:67px;background:#ececec;border:1px solid var(--line);font-size:20px;color:#999;padding:13px 0 0 35px}
.quote .mark{position:absolute;font-size:26px;color:#bbb;font-family:Georgia,serif}
.quote-tail{left:645px;top:416px}
.author{right:21px;top:445px;text-align:right}
.author .name{font-size:16px;color:#666}
.author .role{font-size:6px;color:#666;letter-spacing:.3px}

.section-title{left:22px;top:502px;width:671px;display:flex;align-items:center;gap:10px;font-size:16px;color:#333}
.section-title .rule{flex:1;height:1px;background:var(--line)}
.offer-ring{width:150px;height:150px;border-radius:50%;background:#ececec;top:541px}
.offer-photo{width:130px;height:130px;border-radius:50%;top:551px}
.offer-label{width:147px;height:34px;background:#2d2d2d;color:var(--white);font-size:14px;text-align:center;line-height:34px;top:644px}
.pager{top:607px;width:8px;height:8px;background:#ddd}

.col h3{font-size:16px;color:#444;margin-bottom:10px}
.col .lead{font-weight:bold;color:#333}
.col p{margin-bottom:5px}
.col ul{list-style:none;margin-bottom:5px}
.col li::before{content:"";display:inline-block;width:3px;height:3px;background:var(--teal);margin:0 6px 1px 4px}
.readmore{font-size:10px;color:#333;display:flex;align-items:center;gap:5px}

.recent{left:506px;top:708px;width:187px;height:197px;background:var(--teal);border:2px solid var(--teal-dark);color:var(--white);padding:8px 9px}
.recent h3{font-size:16px;border-left:3px solid #9ab;padding-left:8px;margin-bottom:10px}
.item{display:flex;gap:8px;margin-bottom:6px}
.item .pic{width:60px;height:60px;background:var(--white);border:1px solid #8aa;flex:none}
.item .t{font-size:9px}
.item .d{font-size:7px;color:#9bb}
.item .c{font-size:8px;margin:2px 0}
.price{display:inline-block;background:#6b8996;font-size:8px;font-weight:bold;padding:2px 5px}
.hot{left:654px;top:702px}

.lower{left:0;top:925px;width:714px;height:226px;background:var(--band);border-top:5px solid #e2e2e2}
.block-title{font-size:16px;color:#333;border-left:3px solid var(--teal);padding-left:9px;line-height:15px}
.tags{display:flex;flex-wrap:wrap;gap:7px 5px;width:200px}
.tag{font-size:6.5px;background:var(--white);border:1px solid #ccc;border-right:3px solid var(--teal);padding:3px 4px;color:#555}
.news h4{font-size:8px;color:var(--teal-dark);margin:6px 0 2px}
.map{left:489px;top:986px;width:200px;height:88px;background:radial-gradient(ellipse at center,#bdbdbd 0%,#d4d4d4 60%,#e8e8e8 100%)}
.add{right:22px;top:1105px;font-size:10px;color:#444;display:flex;align-items:center;gap:4px}
.plus{width:10px;height:10px;border-radius:50%;background:#333}

.footer{left:0;top:1151px;width:714px;height:49px;background:var(--bar);color:#777;font-size:11px}
.footer .links{position:absolute;left:22px;top:14px}
.footer .links span{margin:0 5px;color:#444}
.footer .copy{position:absolute;left:410px;top:14px}
</style>
</head>
<body>

<div class="abs topbar">
  <span>SINGUP</span><span class="sep"></span><span>LOGIN</span>
  <span class="social"></span><span class="social"></span><span class="social"></span><span class="social"></span><span class="social"></span>
</div>
<div class="abs header"></div>
<nav class="abs nav cond"><span class="active">HOME</span><span class="slash">/</span>TEMPLATE FEATURES<span class="slash">/</span>SUBPAGE<span class="slash">/</span>EXTENSIONS<span class="slash">/</span>RTL LANGUAGES</nav>

<div class="abs slider-area"></div>
<div class="abs slide-photo" role="img" aria-label="Shoes collection banner: close-up of pink and black high heels"></div>
<div class="abs caption">
  <h2 class="cond">SHOES COLLECTION</h2>
  <p>Lorem ipsum dolor sit amet, consectetur adipiscing elit. Nam vitae augue sapien.</p>
  <div class="more cond">READ MORE <span class="arrow-box"></span></div>
</div>
<div class="abs tab cond" style="top:106px"><div class="thumb" role="img" aria-label="Woman trying on a top" style="background:linear-gradient(90deg,#c89a8a,#d05a9a)"></div>TRY THIS ON</div>
<div class="abs tab active cond" style="top:155px"><div class="thumb" role="img" aria-label="Shoes collection thumbnail" style="background:linear-gradient(90deg,#7a2a6a,#1b1b1b,#c22a3a)"></div>SHOES COLLECTION</div>
<div class="abs tab cond" style="top:204px"><div class="thumb" role="img" aria-label="Local clothing store interior" style="background:linear-gradient(90deg,#eee,#8a6a7a,#ddd)"></div>LOCAL STORE</div>
<div class="abs tab cond" style="top:253px"><div class="thumb" role="img" aria-label="Woman shopping" style="background:linear-gradient(90deg,#6a8aa0,#c9a080)"></div>SHOPPING FRENZY</div>

<blockquote class="abs quote cond">
  <span class="mark" style="left:18px;top:4px">&ldquo;</span>
  Sed ut perspiciatis unde omnis iste natus error sit voluptatem accusantium iste.
  <span class="mark" style="right:16px;top:30px">&rdquo;</span>
</blockquote>
<svg class="abs quote-tail" width="24" height="14" viewBox="0 0 24 14"><path d="M0 0 L12 13 L24 0" fill="#ececec" stroke="#d8d8d8"/><rect x="1" y="0" width="22" height="1.5" fill="#ececec"/></svg>
<div class="abs author"><div class="name cond">Jane Doe</div><div class="role">FURNITURE COMPANY</div></div>

<div class="abs section-title cond"><span class="rule"></span>LATEST HOT OFFERS<span class="rule"></span></div>
<div class="abs pager" style="left:6px"></div><div class="abs pager" style="left:700px"></div>
<div class="abs offer-ring" style="left:24px"></div>
<div class="abs offer-photo" role="img" aria-label="Pink t-shirt" style="left:34px;background:radial-gradient(circle,#f06a78 0%,#f59aa3 35%,#fff 60%)"></div>
<div class="abs offer-label cond" style="left:25px">PINK T-SHIRT</div>
<div class="abs offer-ring" style="left:196px"></div>
<div class="abs offer-photo" role="img" aria-label="Trendy shirt dress" style="left:206px;background:radial-gradient(circle,#8a7d78 0%,#b8aca6 35%,#fff 60%)"></div>
<div class="abs offer-label cond" style="left:198px">TRENDY PINK DRESS</div>
<div class="abs offer-ring" style="left:369px"></div>
<div class="abs offer-photo" role="img" aria-label="Light blue jeans" style="left:379px;background:radial-gradient(circle,#9ab8d4 0%,#c3d6e6 35%,#fff 60%)"></div>
<div class="abs offer-label cond" style="left:371px">REGULAR JEANS</div>
<div class="abs offer-ring" style="left:542px"></div>
<div class="abs offer-photo" role="img" aria-label="Black high heel sandals" style="left:552px;background:radial-gradient(circle,#222 0%,#666 30%,#fff 58%)"></div>
<div class="abs offer-label cond" style="left:543px">HIGH HEELS</div>

<article class="abs col" style="left:22px;top:712px;width:223px">
  <h3 class="cond">LATEST FASHION TRENDS</h3>
  <p class="lead">Lorem ipsum dolor sit amet, consectet dipisicing elit ullamco laboris dolor.</p>
  <p>Nulla egestas pretium augue, nec consequat diam iaculis vitae. Class aptent taciti sociosqu ad litora torquent per conubia nostra, per inceptos himenaeos.</p>
  <ul><li>Sed do eiusmod tempor incididunt ut</li><li>Labore et dolore magna aliqua</li><li>Ut enim ad minim veniam, quis nostrud</li></ul>
  <p>Praesent eu orci eu arcu ultrices ornare sed vel quam. Nunc consequat risus dolor donec nisl sapien, dignissim.</p>
  <div class="readmore cond" style="margin-top:8px">READ MORE... <span class="arrow-box"></span></div>
</article>
<article class="abs col" style="left:263px;top:712px;width:222px">
  <h3 class="cond">FASHION WEEK</h3>
  <p class="lead">Lorem ipsum dolor sit amet, consectet adipisicing elit ullamco laboris.</p>
  <p>In in sem ligula. Ut auctor lorem vel urna vestibulum non semper eros feugiat. Praesent eu orci eu arcu ultrices.</p>
  <p>Class aptent taciti sociosqu ad litora torquent per conubia nostra, per inceptos himenaeos. Sed ultrices adipiscing elit sed mattis ornare sed vel quam.</p>
  <p>Lorem ipsum dolor sit amet, consectetur adipiscing elit. Nulla egestas pretium augue, nec consequat diam iaculis vitae consequat risus dolor.</p>
  <div class="readmore cond" style="margin-top:8px">READ MORE... <span class="arrow-box"></span></div>
</article>

<aside class="abs recent">
  <h3 class="cond">MOST RECENT ITEMS</h3>
  <div class="item"><div class="pic" role="img" aria-label="Dark stylish suit" style="background:linear-gradient(#fff 10%,#333 30%,#333 90%,#fff)"></div>
    <div><div class="t cond" style="font-weight:400">STYLISH SUIT</div><div class="d">2013-01-07 16:44:42</div><div class="c">&#9656; Elegant</div><span class="price">580 EUR</span></div></div>
  <div class="item"><div class="pic" role="img" aria-label="Pink shirt with tie" style="background:linear-gradient(#fff 10%,#c9a3c9 35%,#8a5a8a 70%,#fff)"></div>
    <div><div class="t cond" style="font-weight:400">PINK SHIRT WITH TIE</div><div class="d">2013-01-07 16:42:59</div><div class="c">&#9656; Elegant</div><span class="price">109 EUR</span></div></div>
</aside>
<svg class="abs hot" width="46" height="36" viewBox="0 0 46 36"><path d="M0 0 H18 L46 28 V36 Z" fill="var(--hot)"/><text x="26" y="16" fill="#fff" font-size="7" font-family="Arial" transform="rotate(45 26 16)">HOT</text></svg>

<section class="abs lower"></section>
<div class="abs" style="left:22px;top:955px">
  <div class="block-title cond" style="margin-bottom:14px">CATEGORIES</div>
  <div class="tags">
    <span class="tag">WOMEN</span><span class="tag">SHOES</span><span class="tag">ELEGANT</span><span class="tag">CASUAL</span>
    <span class="tag">DRESSES</span><span class="tag">SWEATERS</span><span class="tag">OUTERWEAR</span>
    <span class="tag">MEN</span><span class="tag">SHOES</span><span class="tag">ELEGANT</span><span class="tag">CASUAL</span>
    <span class="tag">PANTS</span><span class="tag">SHIRTS</span><span class="tag">SWEATERS</span><span class="tag">BAGS</span>
    <span class="tag">OUTERWEAR</span><span class="tag">ACCESSORIES</span><span class="tag">BELTS</span>
    <span class="tag">HATS &amp; SCARVES</span><span class="tag">GLASSES</span>
  </div>
</div>
<div class="abs news" style="left:252px;top:955px;width:212px">
  <div class="block-title cond" style="margin-bottom:8px">LATEST NEWS</div>
  <h4>Be Young Forever</h4>
  <p>Lorem ipsum dolor sit amet, consectetur adipiscing elit. Curabitur pretium odio ac diam sodales semper. In eget augue a leo convallis suscipit at in lorem. Nam pulvinar ultrices nisi, vitae dignissim est rutrum vitae.</p>
  <h4>Shopping in Paris</h4>
  <p>Nunc lacinia mattis egestas. Quisque fermentum diam at lacus dignissim non iaculis urna commodo. Phasellus lacinia auctor sem quis posuere. Duis fermentum blandit tempor.</p>
</div>
<div class="abs" style="left:482px;top:955px"><div class="block-title cond">CHECK ADS IN YOUR AREA</div></div>
<div class="abs map" role="img" aria-label="Dotted world map with location pins"></div>
<div class="abs add cond">ADD YOUR ITEMS <span class="plus"></span></div>

<footer class="abs footer cond">
  <div class="links">Home<span>|</span>Template Features<span>|</span>Subpage<span>|</span>Extensions<span>|</span>RTL Languages</div>
  <div class="copy">Copyrights 2012. All rights reserved.</div>
</footer>

</body>
</html>
```